Hispanic Financial Counseling and Advocate Firm seeks business card design

Looking for a clean, professional business card design. This is a firm that specializes in providing financial education, coaching, and planning to the Hispanic community. The name of the company is Valemar, which means to prosper. We need a design that is clean, professional, and invokes trust, professionalism, but also welcoming. Our logo is a plant growing from a hand to give the messaging of of being in control of growing your financial future and security. Its part of a larger organization names Celesta Financial Group, who's logo is a tree with multi colored branches. We have the back of the card designed so we just need the front designed. the back is blue, so front needs to be a different background color, not blue.

Target Market(s)

Hispanic Community looking to better their future

Industry/Entity Type

financial services

Contact Information for Business Card

contact info: Anselmo Ibarra Jr, 951-555-0147, info@celestafinancialgroup.example. Celestafinancialgroup.example. tag line: Para un futuro mas seguro!

Requirements
Must have
• basics: logo, contact info.
Nice to have
• possibly incorporate the tree logo provided somehow
Should not have
• should not look like the back, needs to be different from the back provided.

```html
<!DOCTYPE html>
<html lang="es">
<head>
<meta charset="utf-8">
<title>Valemar — Tarjeta de presentación</title>
<link rel="stylesheet" href="https://fonts.googleapis.com/css2?family=Montserrat:wght@500;600&family=Nunito:wght@800&family=Roboto:wght@400&display=swap">
<style>
  :root{
    --page:#c4c5c7;
    --navy:#052c42;
    --navy-soft:#0e3b55;
    --white:#ffffff;
    --green:#5aa02c;
    --green-soft:#e4efd9;
    --ink:#3d3f45;
    --slate:#4a5872;
    --drop-green:#8cc63f;
    --drop-blue:#29a9e1;
    --drop-red:#ef4046;
    --drop-purple:#9b7fc1;
    --drop-yellow:#fbc20f;
  }
  *{box-sizing:border-box;margin:0;padding:0}
  html,body{width:900px;height:1200px;overflow:hidden;background:var(--page)}
  .card{position:absolute;left:163px;width:574px;height:369px;border-radius:30px;overflow:hidden}
  .card--back{top:208px;background:var(--navy)}
  .card--front{top:622px;background:var(--white)}

  /* back */
  .parent-mark{position:absolute;left:96px;top:135px;width:100px;height:100px;border-radius:50%;background:var(--navy-soft)}
  .card--back .divider{position:absolute;left:224px;top:108px;width:1.5px;height:153px;background:rgba(255,255,255,.85)}
  .parent-name{position:absolute;left:246px;top:146px;color:var(--white);font-family:"Montserrat",sans-serif;font-weight:500;font-size:28px;line-height:36px;letter-spacing:.3px}
  .services{position:absolute;left:0;right:0;top:294px;text-align:center;color:var(--white);font-family:"Roboto",sans-serif;font-size:16px;line-height:20px}
  .services li{list-style:none;display:inline-flex;align-items:center;margin:0 2px}
  .services svg{width:8px;height:13px;margin-right:5px}

  /* front */
  .brand-mark{position:absolute;left:105px;top:100px;width:80px;height:80px;border-radius:50%;background:var(--green-soft)}
  .front-name{position:absolute;left:40px;width:210px;top:200px;text-align:center;color:var(--green);font-family:"Montserrat",sans-serif;font-weight:600;font-size:40px;line-height:48px}
  .card--front .divider{position:absolute;left:285px;top:81px;width:1.5px;height:208px;background:var(--slate)}
  .contact{position:absolute;left:308px;top:117px;width:226px}
  .contact__name{font-family:"Nunito",sans-serif;font-weight:800;color:var(--green);font-size:22px;letter-spacing:.5px;line-height:28px;white-space:nowrap}
  .contact__role{font-family:"Roboto",sans-serif;color:var(--ink);font-size:13.5px;margin-top:4px}
  .contact__rule{height:1.5px;background:var(--green);width:212px;margin:8px 0 10px}
  .contact__list li{list-style:none;display:flex;align-items:center;font-family:"Roboto",sans-serif;color:var(--ink);font-size:12.5px;letter-spacing:0;line-height:23.5px;white-space:nowrap}
  .contact__list svg{width:10px;height:10px;margin-right:4px;flex:none}
  .tagline{position:absolute;left:0;right:0;top:330px;text-align:center;color:var(--green);font-family:"Montserrat",sans-serif;font-weight:600;font-size:14px;letter-spacing:.4px}
</style>
</head>
<body>

<section class="card card--back" aria-label="Reverso de la tarjeta">
  <span class="parent-mark"></span>
  <span class="divider"></span>
  <h1 class="parent-name">Celesta<br>Financial Group Inc</h1>
  <ul class="services">
    <li><svg viewBox="0 0 8 13"><path d="M4 0C6 4 8 7 8 9a4 4 0 0 1-8 0C0 7 2 4 4 0z" fill="var(--drop-green)"/></svg>Inmigración</li>
    <li><svg viewBox="0 0 8 13"><path d="M4 0C6 4 8 7 8 9a4 4 0 0 1-8 0C0 7 2 4 4 0z" fill="var(--drop-blue)"/></svg>Planificacion Financiera</li><br>
    <li><svg viewBox="0 0 8 13"><path d="M4 0C6 4 8 7 8 9a4 4 0 0 1-8 0C0 7 2 4 4 0z" fill="var(--drop-red)"/></svg>Seguros</li>
    <li><svg viewBox="0 0 8 13"><path d="M4 0C6 4 8 7 8 9a4 4 0 0 1-8 0C0 7 2 4 4 0z" fill="var(--drop-purple)"/></svg>Impuestos</li>
    <li><svg viewBox="0 0 8 13"><path d="M4 0C6 4 8 7 8 9a4 4 0 0 1-8 0C0 7 2 4 4 0z" fill="var(--drop-red)"/></svg>Y mas</li><br>
    <li><svg viewBox="0 0 8 13"><path d="M4 0C6 4 8 7 8 9a4 4 0 0 1-8 0C0 7 2 4 4 0z" fill="var(--drop-yellow)"/></svg>Preparación de documentos</li>
  </ul>
</section>

<section class="card card--front" aria-label="Frente de la tarjeta">
  <span class="brand-mark"></span>
  <h2 class="front-name">Valemar</h2>
  <span class="divider"></span>
  <div class="contact">
    <p class="contact__name">Anselmo Ibarra Jr</p>
    <p class="contact__role">Director</p>
    <div class="contact__rule"></div>
    <ul class="contact__list">
      <li><svg viewBox="0 0 12 12"><path d="M2.5 0.5l2 2.4-1.2 1.4a7 7 0 0 0 4.4 4.4l1.4-1.2 2.4 2-1.3 1.9C5 11.2 0.8 7 0.6 1.8z" fill="var(--green)"/></svg>951-555-0147</li>
      <li><svg viewBox="0 0 12 12"><rect x="0.5" y="2" width="11" height="8" fill="var(--green)"/><path d="M0.5 2l5.5 4.5L11.5 2" stroke="#fff" stroke-width="1" fill="none"/></svg>info@celestafinancialgroup.example</li>
      <li><svg viewBox="0 0 12 12"><circle cx="6" cy="6" r="5" fill="none" stroke="var(--green)" stroke-width="1.2"/><path d="M1 6h10M6 1c-2.5 3-2.5 7 0 10M6 1c2.5 3 2.5 7 0 10" stroke="var(--green)" stroke-width="1" fill="none"/></svg>www.celestafinancialgroup.example</li>
    </ul>
  </div>
  <p class="tagline">PARA UN FUTURO MÁS SEGURO!</p>
</section>

</body>
</html>
```